A website serving business owners or those wishing to become business owners.

A website serving those in the service industry or would like to get started with their own business. From business licensing , marketing, business loans, and much more.

We offer business incubation services as well as further growth assistance.

Including, but not limited to...

marketing
websites
seo
Search Ads
social media ads
logos
business licensing assistance
customer acquisition and ongoing coordination
1. scheduling
2 customer support
3.coordination between business owners and clients

Cleaning training program/courses.

Target Market(s)

Hispanic folks looking to start or grow their cleaning company.

Industry/Entity Type

business incubation and growth support.

Font styles to use
Sans Serif

Requirements
Must have
• wordpress, custom design
Nice to have
• something similar to this .... https://www.velmarkhub.example/
Should not have
• no predesigned themes, no third party templates

```html
<!DOCTYPE html>
<html lang="en">
<head>
<meta charset="utf-8">
<title>Velmark Hub — Business Growth Support</title>
<link rel="stylesheet" href="https://fonts.googleapis.com/css2?family=Montserrat:wght@600;700;800&family=Roboto:wght@400;500;700&display=swap">
<style>
:root{
  --navy:#16234a;
  --navy-2:#1b2a57;
  --blue:#3d86f5;
  --blue-soft:#5b97f5;
  --ink:#1d1f26;
  --grey:#5d6472;
  --light:#f1f2f5;
  --white:#ffffff;
}
*{box-sizing:border-box;margin:0;padding:0}
html,body{width:1200px;height:4918px;overflow:hidden}
body{font-family:"Roboto",sans-serif;color:var(--ink);background:var(--white);position:relative}
h1,h2,h3,.brand,.btn{font-family:"Montserrat",sans-serif}
section,header,footer{position:absolute;left:0;width:1200px}
.abs{position:absolute}
.btn{position:absolute;display:flex;align-items:center;justify-content:center;gap:8px;background:var(--blue);color:#fff;font-size:13px;font-weight:700;border-radius:24px;text-transform:uppercase;letter-spacing:.2px}
.btn .arr{width:13px;height:13px;border-radius:50%;background:#fff;position:relative}
.btn .arr::after{content:"";position:absolute;left:3px;top:4px;border:3px solid transparent;border-left:5px solid var(--blue)}
.btn.dark{background:var(--navy)}
.btn.dark .arr::after{border-left-color:var(--navy)}

/* header */
.site-header{top:0;height:80px;background:var(--navy)}
.brand{position:absolute;display:flex;align-items:center;gap:10px;color:#fff;font-weight:800;font-size:19px}
.brand .mark{width:30px;height:30px;border-radius:50%;background:var(--blue)}
.nav{position:absolute;left:475px;top:30px;display:flex;gap:29px;font-size:13px;font-weight:500;color:#fff}
.login{left:960px;top:22px;width:95px;height:35px;border-radius:4px;font-size:13px;text-transform:none}

/* hero */
.hero{top:80px;height:597px;background:linear-gradient(90deg,#1e2432 0%,#333a48 35%,#58606d 60%,#7c8592 100%)}
.hero .eyebrow{left:140px;top:167px;color:var(--blue-soft);font-size:14px;font-weight:500}
.hero h1{left:143px;top:202px;width:440px;color:#fff;font-size:37px;line-height:45px;font-weight:700}

/* services */
.services{top:677px;height:720px;background:radial-gradient(ellipse at 60% 40%,#ffffff 0%,#f4f6fa 60%,#e9edf4 100%)}
.section-title{position:absolute;left:0;width:1200px;text-align:center;font-size:32px;font-weight:700;color:var(--ink)}
.hex{position:absolute;width:84px;height:92px;background:var(--navy);clip-path:polygon(50% 0,100% 25%,100% 75%,50% 100%,0 75%,0 25%);display:flex;align-items:center;justify-content:center}
.hex.active{background:var(--blue)}
.svc-label{position:absolute;font-size:16px;font-weight:500;color:var(--ink);line-height:19px}
.svc-label.right-align{text-align:right}

/* feature rows */
.feature{height:574px}
.feature h2{position:absolute;font-size:33px;font-weight:700;line-height:38px}
.ring{position:absolute;border-radius:50%;border:2px solid var(--blue)}
.photo{position:absolute;border-radius:50%}
.badge{position:absolute;width:100px;height:100px;border-radius:50%;background:var(--blue);border:5px solid #fff;display:flex;align-items:center;justify-content:center}
.checks{position:absolute;list-style:none;font-size:12.5px;line-height:21px;color:var(--grey)}
.checks li{position:relative;padding-left:23px;margin-bottom:10px}
.checks li::before{content:"";position:absolute;left:0;top:4px;width:13px;height:13px;border-radius:50%;background:var(--blue)}
.checks li::after{content:"";position:absolute;left:4px;top:6px;width:3px;height:6px;border:solid #fff;border-width:0 2px 2px 0;transform:rotate(45deg)}
.support{background:var(--navy)}
.support h2{color:#fff}
.support .checks{color:#e4e8f2}

/* why */
.why{top:3100px;height:439px;background:var(--light)}
.stat{position:absolute;display:flex;gap:22px}
.stat .ic{width:60px;height:60px}
.stat b{display:block;font-size:19px;font-weight:700;margin-bottom:6px}
.stat span{display:block;font-size:12px;color:var(--grey);line-height:16px;width:150px}

/* cta */
.cta{top:3539px;height:273px;background:linear-gradient(100deg,#3f86f4,#5394f6 60%,#3f86f4)}
.cta h2{position:absolute;left:0;width:1200px;top:52px;text-align:center;color:#fff;font-size:31px;line-height:41px;font-weight:700}

/* blog */
.blog{top:3812px;height:773px}
.card{position:absolute;width:303px;height:269px;background:#fff;box-shadow:0 3px 14px rgba(20,30,60,.08);padding:26px 20px}
.card time{display:flex;align-items:center;gap:5px;color:var(--blue);font-size:12px;font-weight:500}
.card time::before{content:"";width:10px;height:10px;border:1.5px solid var(--blue);border-radius:50%}
.card h3{font-family:"Roboto",sans-serif;font-size:14px;font-weight:700;line-height:21px;margin:9px 0 12px}
.card p{font-size:12px;color:var(--grey);line-height:21px}
.card .btn{left:20px;bottom:26px;width:134px;height:33px;font-size:12px}
.blog-img{position:absolute;width:303px;height:269px}

/* footer */
.site-footer{top:4585px;height:333px;background:var(--navy);color:#fff}
.site-footer h4{position:absolute;font-size:14px;font-weight:700}
.links{position:absolute;list-style:none;font-size:12px;line-height:24px;color:#d5daea}
.social{position:absolute;left:170px;top:4757px;display:flex;gap:9px}
.social i{width:28px;height:28px;border:1.5px solid #fff;border-radius:50%;display:block}
.contact{position:absolute;left:836px;font-size:12px;color:#d5daea;line-height:18px;padding-left:22px}
.contact b{display:block;color:#fff;font-size:11px}
.contact svg{position:absolute;left:0;top:2px}
.copy{position:absolute;left:0;width:1200px;top:4878px;text-align:center;font-size:13px;color:#d5daea}
.to-top{position:absolute;left:1073px;top:4836px;width:32px;height:32px;border-radius:50%;background:var(--blue)}
</style>
</head>
<body>

<header class="site-header">
  <div class="brand" style="left:143px;top:25px"><span class="mark"></span>VELMARK HUB</div>
  <nav class="nav"><span>Home</span><span>Services</span><span>Success Stories</span><span>Pricing</span><span>About</span><span>Blog</span></nav>
  <span class="btn login">Login</span>
</header>

<section class="hero">
  <div class="abs" role="img" aria-label="Team of business people collaborating around a laptop in a bright office" style="left:520px;top:0;width:680px;height:597px;background:linear-gradient(90deg,rgba(60,66,80,0),rgba(140,150,165,.45))"></div>
  <p class="abs eyebrow">We help you launch, grow and scale</p>
  <h1 class="abs">Guiding Your Business Journey, Every Step of the Way</h1>
  <span class="btn" style="left:145px;top:378px;width:183px;height:49px">Get Started <i class="arr"></i></span>
</section>

<section class="services">
  <h2 class="section-title" style="top:63px">Our Services</h2>
  <div class="abs" role="img" aria-label="Smiling woman seated cross-legged with a laptop, pointing to the services" style="left:505px;top:135px;width:230px;height:415px;border-radius:115px 115px 40px 40px;background:linear-gradient(180deg,#c9b3a3 0%,#f4f4f4 40%,#c8ccd2 60%,#3d5a80 100%)"></div>
  <svg class="abs" style="left:0;top:0" width="1200" height="720" fill="none" stroke="#1b2a57" stroke-width="2">
    <path d="M475 201 H540 V223"/><circle cx="540" cy="224" r="4" fill="#1b2a57"/>
    <path d="M760 201 H675 V223"/><circle cx="760" cy="201" r="4" fill="#3d86f5" stroke="none"/>
    <path d="M416 320 H525"/><circle cx="406" cy="320" r="4" fill="#3d86f5" stroke="none"/>
    <path d="M790 320 H700"/><circle cx="787" cy="320" r="4" fill="#3d86f5" stroke="none"/>
    <path d="M420 423 H510 V385"/>
    <path d="M780 410 H690 V385"/><circle cx="780" cy="410" r="4" fill="#3d86f5" stroke="none"/>
  </svg>
  <div class="hex" style="left:349px;top:155px"><svg width="36" height="36" fill="none" stroke="#fff" stroke-width="2"><rect x="6" y="4" width="24" height="14" rx="2"/><circle cx="18" cy="25" r="4"/><path d="M10 34c2-4 14-4 16 0"/></svg></div>
  <div class="svc-label right-align" style="left:200px;top:191px;width:130px">Search Ads</div>
  <div class="hex" style="left:782px;top:155px"><svg width="36" height="36" fill="none" stroke="#fff" stroke-width="2"><rect x="4" y="6" width="28" height="20" rx="2"/><path d="M12 32h12M18 26v6M9 20l6-6 4 4 7-7"/></svg></div>
  <div class="svc-label" style="left:878px;top:191px">Marketing</div>
  <div class="hex" style="left:291px;top:268px"><svg width="36" height="36" fill="none" stroke="#fff" stroke-width="2"><rect x="4" y="4" width="12" height="12"/><rect x="20" y="20" width="12" height="12"/><path d="M16 10h10v10M10 16v10h10"/></svg></div>
  <div class="svc-label right-align" style="left:120px;top:294px;width:150px">Social Media<br>Ads</div>
  <div class="hex" style="left:824px;top:268px"><svg width="36" height="36" fill="none" stroke="#fff" stroke-width="2"><circle cx="18" cy="18" r="13"/><path d="M11 18h14M18 11v14"/></svg></div>
  <div class="svc-label" style="left:922px;top:304px">Websites</div>
  <div class="hex" style="left:315px;top:387px"><svg width="36" height="36" fill="none" stroke="#fff" stroke-width="2"><circle cx="18" cy="14" r="8"/><path d="M8 32c2-8 18-8 20 0"/></svg></div>
  <div class="svc-label right-align" style="left:180px;top:423px;width:115px">Logos</div>
  <div class="hex active" style="left:798px;top:387px"><svg width="36" height="36" fill="none" stroke="#fff" stroke-width="2"><circle cx="16" cy="16" r="10"/><path d="M23 23l9 9"/></svg></div>
  <div class="svc-label" style="left:896px;top:425px">SEO</div>
  <span class="btn" style="left:488px;top:605px;width:210px;height:44px">View All Services <i class="arr"></i></span>
</section>

<section class="feature" style="top:1397px">
  <div class="ring" style="left:146px;top:73px;width:430px;height:430px"></div>
  <div class="photo" role="img" aria-label="Business team reviewing work together on a laptop" style="left:164px;top:91px;width:394px;height:394px;background:linear-gradient(135deg,#9aa3ad,#4f5866 60%,#2c3340)"></div>
  <div class="badge" style="left:475px;top:362px"><svg width="44" height="44" fill="none" stroke="#fff" stroke-width="2.2"><rect x="5" y="8" width="28" height="26" rx="3"/><path d="M5 16h28M12 4v7M26 4v7"/><circle cx="32" cy="32" r="8" fill="#3d86f5"/><path d="M28 32l3 3 5-5"/></svg></div>
  <h2 style="left:647px;top:94px">Scheduling</h2>
  <ul class="checks" style="left:647px;top:159px;width:410px">
    <li>Lorem ipsum dolor sit amet, consectetur adipiscing elit, sed do tempor incididunt ut labore et dolore magna aliqua.</li>
    <li>Ut enim ad minim veniam, quis nostrud exercitation ullamco nisi ex ea commodo consequat.</li>
    <li>Duis aute irure dolor in reprehenderit in voluptate velit</li>
    <li>Sed ut perspiciatis unde omnis iste natus error sit voluptatem</li>
    <li>Lorem ipsum dolor sit amet, consectetur adipiscing elit, sed do tempor incididunt ut labore et dolore magna aliqua.</li>
    <li>Duis aute irure dolor in reprehenderit in voluptate velit</li>
  </ul>
  <span class="btn" style="left:647px;top:435px;width:168px;height:44px">Learn More <i class="arr"></i></span>
</section>

<section class="feature support" style="top:1971px;height:532px">
  <h2 style="left:143px;top:70px">Customer Support</h2>
  <ul class="checks" style="left:143px;top:137px;width:420px">
    <li>Lorem ipsum dolor sit amet, consectetur adipiscing elit, sed do tempor incididunt ut labore et dolore magna aliqua.</li>
    <li>Ut enim ad minim veniam, quis nostrud exercitation ullamco nisi ex ea commodo consequat.</li>
    <li>Duis aute irure dolor in reprehenderit in voluptate velit</li>
    <li>Sed ut perspiciatis unde omnis iste natus error sit voluptatem</li>
    <li>Lorem ipsum dolor sit amet, consectetur adipiscing elit, sed do tempor incididunt ut labore et dolore magna aliqua.</li>
    <li>Duis aute irure dolor in reprehenderit in voluptate velit</li>
  </ul>
  <span class="btn" style="left:143px;top:412px;width:168px;height:44px">Learn More <i class="arr"></i></span>
  <div class="ring" style="left:625px;top:43px;width:430px;height:430px"></div>
  <div class="photo" role="img" aria-label="Support agent with headset smiling at a computer in a call centre" style="left:643px;top:61px;width:394px;height:394px;background:linear-gradient(135deg,#c9d3de,#8d9aab 55%,#3f4a5c)"></div>
  <div class="badge" style="left:633px;top:341px"><svg width="44" height="44" fill="none" stroke="#fff" stroke-width="2.2"><circle cx="22" cy="16" r="8"/><path d="M10 18v-3a12 12 0 0 1 24 0v3M8 40c2-9 26-9 28 0"/></svg></div>
</section>

<section class="feature" style="top:2503px;height:597px">
  <div class="ring" style="left:146px;top:81px;width:430px;height:430px"></div>
  <div class="photo" role="img" aria-label="Business owner and client talking and smiling at a desk" style="left:164px;top:99px;width:394px;height:394px;background:linear-gradient(135deg,#d9dde2,#7c8592 50%,#2d3442)"></div>
  <div class="badge" style="left:465px;top:366px"><svg width="44" height="44" fill="none" stroke="#fff" stroke-width="2.2"><circle cx="22" cy="14" r="7"/><circle cx="10" cy="34" r="5"/><circle cx="34" cy="34" r="5"/><path d="M22 21v6M14 31l6-4M30 31l-6-4"/></svg></div>
  <h2 style="left:647px;top:94px;width:400px">Coordination Between Business Owners and Clients</h2>
  <ul class="checks" style="left:647px;top:235px;width:410px">
    <li>Lorem ipsum dolor sit amet, consectetur adipiscing elit, sed do tempor incididunt ut labore et dolore magna aliqua.</li>
    <li>Ut enim ad minim veniam, quis nostrud exercitation ullamco nisi ex ea commodo consequat.</li>
    <li>Duis aute irure dolor in reprehenderit in voluptate velit</li>
    <li>Sed ut perspiciatis unde omnis iste natus error sit voluptatem</li>
    <li>Duis aute irure dolor in reprehenderit in voluptate velit</li>
  </ul>
  <span class="btn" style="left:647px;top:449px;width:168px;height:44px">Learn More <i class="arr"></i></span>
</section>

<section class="why">
  <h2 class="abs" style="left:143px;top:76px;font-size:34px;font-weight:700">Why Choose Us?</h2>
  <svg class="abs" style="left:0;top:0" width="700" height="439"><line x1="362" y1="185" x2="362" y2="375" stroke="#d3d6dc"/><line x1="143" y1="258" x2="610" y2="258" stroke="#d3d6dc"/></svg>
  <div class="stat" style="left:143px;top:200px"><svg class="ic" fill="none" stroke="#e2473b" stroke-width="2"><rect x="6" y="20" width="22" height="22"/><rect x="30" y="30" width="22" height="22"/><rect x="18" y="4" width="22" height="18"/></svg><div><b>50+</b><span>Items in Home Services</span></div></div>
  <div class="stat" style="left:387px;top:200px"><svg class="ic" fill="none" stroke="#f2b928" stroke-width="2"><rect x="6" y="24" width="46" height="26" rx="3"/><circle cx="29" cy="14" r="9"/><path d="M14 37h30"/></svg><div><b>100%</b><span>of businesses launched in 7 days</span></div></div>
  <div class="stat" style="left:143px;top:310px"><svg class="ic" fill="none" stroke="#3fa765" stroke-width="2"><path d="M6 20l22-12 22 12v24L28 56 6 44z"/><path d="M6 20l22 12 22-12M28 32v24"/></svg><div><b>1,500</b><span>Community of business owners</span></div></div>
  <div class="stat" style="left:387px;top:310px"><svg class="ic" fill="none" stroke="#3d86f5" stroke-width="2"><circle cx="22" cy="22" r="14"/><circle cx="38" cy="38" r="14"/><path d="M22 15v14M38 31v14"/></svg><div><b>4.9</b><span>Customer satisfaction</span></div></div>
  <div class="abs" role="img" aria-label="Smiling man in a light blue shirt holding an open laptop" style="left:668px;top:29px;width:372px;height:410px;border-radius:180px 180px 0 0;background:linear-gradient(180deg,#caa58a 0%,#dbe4ef 35%,#b9c7d8 70%,#8e9aa8 100%)"></div>
</section>

<section class="cta">
  <h2>We help you launch, grow and scale your home<br>services business.</h2>
  <span class="btn dark" style="left:508px;top:166px;width:183px;height:48px">Get Started <i class="arr"></i></span>
</section>

<section class="blog">
  <h2 class="section-title" style="top:67px">Latest Blog</h2>
  <article class="card" style="left:145px;top:147px"><time>20 Feb, 2024</time><h3>Lorem ipsum dolor sit amet, consectetur adipiscing elit,</h3><p>This former search quality analyst explains the difference between search engine algorithms, manual actions, quality and penalties.</p><span class="btn">Read More <i class="arr"></i></span></article>
  <div class="blog-img" role="img" aria-label="Open-plan office with people working at computers" style="left:450px;top:147px;background:linear-gradient(135deg,#6b7480,#2c333e)"></div>
  <article class="card" style="left:754px;top:147px"><time>20 Feb, 2024</time><h3>Lorem ipsum dolor sit amet, consectetur adipiscing elit,</h3><p>This former search quality analyst explains the difference between search engine algorithms, manual actions, quality and penalties.</p><span class="btn">Read More <i class="arr"></i></span></article>
  <div class="blog-img" role="img" aria-label="Colleagues working side by side on laptops" style="left:145px;top:416px;background:linear-gradient(135deg,#aab1ba,#4b525d)"></div>
  <article class="card" style="left:450px;top:416px"><time>20 Feb, 2024</time><h3>Lorem ipsum dolor sit amet, consectetur adipiscing elit,</h3><p>This former search quality analyst explains the difference between search engine algorithms, manual actions, quality and penalties.</p><span class="btn">Read More <i class="arr"></i></span></article>
  <div class="blog-img" role="img" aria-label="Team meeting around a table in a modern office" style="left:754px;top:416px;background:linear-gradient(135deg,#c3ccd6,#5d6a7a)"></div>
</section>

<footer class="site-footer">
  <div class="brand" style="left:143px;top:99px"><span class="mark"></span>VELMARK HUB</div>
  <h4 style="left:424px;top:52px">Quick Links</h4>
  <ul class="links" style="left:424px;top:87px"><li>Home</li><li>Our Services</li><li>Success Stories</li><li>Pricing</li><li>About</li><li>Blog</li></ul>
  <h4 style="left:616px;top:52px">About Company</h4>
  <ul class="links" style="left:616px;top:87px"><li>Legal Information</li><li>Terms &amp; Condition</li><li>Privacy Police</li><li>Support</li><li>Site Map</li><li>FAQ</li></ul>
  <h4 style="left:836px;top:52px">Contact Us</h4>
  <div class="contact" style="top:88px"><svg width="12" height="12"><path d="M2 1h3l1 3-2 1a7 7 0 0 0 3 3l1-2 3 1v3c-6 1-10-3-9-9z" fill="#3d86f5"/></svg><b>Phone</b>+1 (555) 014-2290</div>
  <div class="contact" style="top:134px"><svg width="13" height="10"><rect width="13" height="10" rx="1" fill="#3d86f5"/><path d="M0 1l6.5 5L13 1" stroke="#fff" fill="none"/></svg><b>Email</b>info@velmarkhub.example</div>
  <div class="contact" style="top:180px;width:250px"><svg width="11" height="14"><path d="M5.5 0A5.5 5.5 0 0 0 0 5.5C0 9 5.5 14 5.5 14S11 9 11 5.5A5.5 5.5 0 0 0 5.5 0z" fill="#3d86f5"/><circle cx="5.5" cy="5.5" r="2" fill="#fff"/></svg><b>Location</b>220 Harbor Lane, Suite 4, Millbrook, NY 10990, USA</div>
</footer>
<div class="social"><i></i><i></i><i></i><i></i></div>
<div class="to-top"><svg width="32" height="32" fill="none" stroke="#fff" stroke-width="2"><path d="M11 18l5-5 5 5"/></svg></div>
<p class="copy">2024 Copyright - Velmark Hub | All Rights Reserved</p>

</body>
</html>
```